Book Cover for Senior Care Agencies

Design a cover [kindle and print] for a book of interviews with home health care agencies, that also has client stories [like a Lantern Tales of Kindness type book]

The title is
Hands That Stay

subtitle
Selecting A Trusted Elder Support Service

The book will have 7 co-authors, so they will need to be listed on the cover
Print book Size 6 x 9

For image, I like the idea of an adult helping their senior parent out... What i am going for is very, clean and crisp yet warm. No cartoons.

I don't tend to like script fonts.
thank you

Target Market(s)

Family members who have senior relatives or parents

Industry/Entity Type

Health Care

Font styles to use
Serif
Sans Serif

Requirements
Should not have
• cartoons

```html
<!DOCTYPE html>
<html lang="en">
<head>
<meta charset="utf-8">
<title>Hands That Stay – Book Cover Wrap</title>
<link rel="stylesheet" href="https://fonts.googleapis.com/css2?family=Fira+Sans:wght@800;900&family=Fira+Sans+Condensed:wght@700&family=Open+Sans:wght@400;700&display=swap">
<style>
  :root {
    --stage: #e9eaeb;
    --spine-blue: #1e96d8;
    --title-blue: #1a7fc4;
    --subtitle-blue: #b3def6;
    --mist-top: #cfe6e6;
    --mist-mid: #8fbcb7;
    --floor-deep: #2c4a40;
    --ink: #1b1f1f;
    --white: #ffffff;
  }
  * { box-sizing: border-box; margin: 0; padding: 0; }
  html, body { width: 1200px; height: 1200px; overflow: hidden; }
  body {
    background: var(--stage);
    display: flex; align-items: center; justify-content: center;
  }
  .wrap { display: flex; height: 750px; box-shadow: 0 10px 30px rgba(0,0,0,.18); }
  .cover { position: relative; width: 500px; height: 750px; overflow: hidden; }
  .cover-scene {
    position: absolute; inset: 0;
    background: linear-gradient(180deg, var(--mist-top) 0%, #b9d8d6 35%, var(--mist-mid) 62%, #4f7a6e 82%, var(--floor-deep) 100%);
  }
  .spine {
    width: 40px; height: 750px; background: var(--spine-blue);
    display: flex; align-items: center; justify-content: center;
  }
  .spine-text {
    writing-mode: vertical-rl;
    font-family: "Fira Sans Condensed", sans-serif; font-weight: 700;
    color: var(--white); font-size: 19px; letter-spacing: .3px; white-space: nowrap;
  }
  /* back */
  .back-photo {
    position: absolute; left: 25px; top: 265px; width: 125px; height: 75px;
    background: linear-gradient(180deg, rgba(40,50,50,.55), rgba(40,50,50,.15));
    border-radius: 4px;
  }
  .back-copy {
    position: absolute; left: 172px; top: 130px; width: 305px;
    font-family: "Open Sans", sans-serif; color: var(--ink);
    font-size: 12.5px; line-height: 1.45; text-align: justify; hyphens: auto;
  }
  .back-copy h2 {
    font-size: 14.5px; font-weight: 700; margin-bottom: 2px;
    text-align: left; white-space: nowrap;
  }
  .back-copy p { margin-bottom: 7px; }
  .back-note {
    position: absolute; left: 30px; bottom: 80px; width: 220px;
    font-family: "Open Sans", sans-serif; font-size: 9.5px; line-height: 1.35; color: var(--white);
  }
  /* front */
  .title {
    position: absolute; left: 0; right: 0; top: 70px; text-align: center;
    font-family: "Fira Sans", sans-serif; font-weight: 900; color: var(--title-blue);
    text-transform: uppercase; line-height: .9;
  }
  .title-line-1 { display: block; font-size: 74px; letter-spacing: -1px; }
  .title-line-2 { display: block; font-size: 150px; letter-spacing: -3px; }
  .front-photo {
    position: absolute; left: 160px; top: 290px; width: 190px; height: 330px;
    background: linear-gradient(180deg, rgba(110,90,80,.55), rgba(60,70,90,.6) 60%, rgba(60,70,90,.25));
    border-radius: 60px 60px 10px 10px;
  }
  .subtitle {
    position: absolute; left: 50px; right: 30px; top: 560px;
    font-family: "Fira Sans Condensed", sans-serif; font-weight: 700;
    color: var(--subtitle-blue); font-size: 38px; line-height: 1.05; text-align: center;
  }
  .authors {
    position: absolute; left: 20px; right: 20px; bottom: 38px; text-align: center;
    font-family: "Open Sans", sans-serif; font-size: 13px; color: var(--white); line-height: 1.5;
  }
</style>
</head>
<body>
  <div class="wrap">
    <section class="cover cover-back">
      <div class="cover-scene" role="img" aria-label="Misty bright hall with reflective floor and a lone figure on a bench"></div>
      <div class="back-photo" role="img" aria-label="Silhouette of a person sitting on a bench"></div>
      <div class="back-copy">
        <h2>Selecting A Trusted Elder Support Service</h2>
        <p>Lorem ipsum dolor sit amet, consectetuer adipiscing elit. Aenean commodo ligula eget dolor. Aenean massa. Cum sociis natoque penatibus et magnis dis parturient montes, nascetur ridiculus mus. Donec quam felis, ultricies nec, pellentesque eu, pretium quis, sem. Nulla consequat massa quis enim. Donec pede justo, fringilla vel.</p>
        <p>Integer tincidunt. Cras dapibus. Vivamus elementum semper nisi. Aenean vulputate eleifend tellus. Aenean leo ligula, porttitor eu, consequat vitae, eleifend ac, enim. Aliquam lorem ante, dapibus in, viverra quis, feugiat a, tellus. Phasellus viverra nulla ut metus varius laoreet.</p>
        <p>Quisque rutrum. Aenean imperdiet. Etiam ultricies nisi vel augue. Curabitur ullamcorper ultricies nisi. Nam eget dui.</p>
        <p>Quis ante. Etiam sit amet orci eget eros faucibus tincidunt. Duis leo. Sed fringilla mauris sit amet nibh. Donec sodales sagittis magna. Sed consequat, leo eget bibendum sodales, augue velit cursus nunc,</p>
      </div>
      <p class="back-note">Quisque rutrum. Aenean imperdiet. Etiam ultricies nisi vel augue. Curabitur ullamcorper ultricies nisi. Nam eget dui.</p>
    </section>
    <aside class="spine">
      <span class="spine-text">HANDS THAT STAY: Selecting A Trusted Elder Support Service</span>
    </aside>
    <section class="cover cover-front">
      <div class="cover-scene" role="img" aria-label="Bright modern hall with blurred people and reflective floor"></div>
      <div class="front-photo" role="img" aria-label="Adult son walking arm in arm with his elderly father who uses a cane"></div>
      <h1 class="title">
        <span class="title-line-1">Hands That</span>
        <span class="title-line-2">Stay</span>
      </h1>
      <p class="subtitle">Selecting A Trusted<br>Elder Support Service</p>
      <p class="authors">Name of Authors • Name of Authors • Name of Authors • Name of Authors<br>Name of Authors • Name of Authors • Name of Authors</p>
    </section>
  </div>
</body>
</html>
```